Business Card for Business consulting practice

Need a design for a consultant business card. Simple and elegant.
I need the following information on the card:
Logo: (see uploaded file)
Company name: Calmora Advisory Group
Name: Dana Weltrup
Title: Managing Director - Aerospace and Defence
Phone #: 514-268-3917
e-mail: dana.weltrup@calmora-example.com
Website: www.calmora-example.com
Tagline: Proposals Management and Capture support for complex procurements

```html
<!DOCTYPE html>
<html lang="en">
<head>
<meta charset="utf-8">
<title>Calmora Advisory Group – Business Card</title>
<link rel="stylesheet" href="https://fonts.googleapis.com/css2?family=Montserrat:wght@400;500;600;700&display=swap">
<style>
  :root {
    --navy: #0d2a40;
    --teal: #2a8fc4;
    --paper: #ffffff;
    --backdrop: #eef1f3;
    --ink: #1d2e3c;
    --muted: #3b4a56;
  }
  * { box-sizing: border-box; margin: 0; padding: 0; }
  html, body { width: 982px; height: 1200px; overflow: hidden; }
  body {
    background: var(--backdrop);
    font-family: "Montserrat", Arial, sans-serif;
    position: relative;
  }
  .card {
    position: absolute;
    left: 111px;
    width: 760px;
    height: 424px;
    box-shadow: 0 6px 22px rgba(13, 42, 64, 0.12);
  }
  /* Front */
  .card-front {
    top: 130px;
    background: var(--navy);
    display: flex;
    align-items: center;
    justify-content: center;
  }
  .wordmark {
    display: flex;
    align-items: center;
    gap: 14px;
  }
  .wordmark-dot {
    border-radius: 50%;
    background: var(--teal);
    flex: none;
  }
  .card-front .wordmark-dot { width: 22px; height: 22px; }
  .card-front .wordmark-name {
    color: var(--paper);
    font-size: 36px;
    font-weight: 600;
    letter-spacing: 0.5px;
  }
  /* Back */
  .card-back {
    top: 634px;
    background: var(--paper);
    border: 2px solid var(--navy);
  }
  .holder {
    position: absolute;
    left: 392px;
    top: 34px;
    padding-left: 20px;
    border-left: 3px solid var(--teal);
    color: var(--ink);
  }
  .holder-name { font-size: 22px; font-weight: 700; line-height: 1.25; }
  .holder-role { font-size: 20px; font-weight: 400; line-height: 1.35; color: var(--muted); }
  .back-wordmark {
    position: absolute;
    left: 48px;
    top: 300px;
    gap: 10px;
  }
  .back-wordmark .wordmark-dot { width: 14px; height: 14px; }
  .back-wordmark .wordmark-name {
    color: var(--navy);
    font-size: 20px;
    font-weight: 600;
  }
  .contacts {
    position: absolute;
    left: 360px;
    top: 258px;
    list-style: none;
    color: var(--ink);
    font-size: 19px;
  }
  .contacts li {
    display: flex;
    align-items: center;
    gap: 12px;
    height: 39px;
  }
  .contacts svg { width: 16px; height: 16px; flex: none; fill: var(--teal); }
  .tagline-band {
    position: absolute;
    left: 0; right: 0; bottom: 0;
    height: 34px;
    background: var(--navy);
    color: var(--paper);
    font-size: 16px;
    font-weight: 500;
    display: flex;
    align-items: center;
    justify-content: center;
    letter-spacing: 0.2px;
  }
</style>
</head>
<body>
  <section class="card card-front" aria-label="Card front">
    <div class="wordmark">
      <span class="wordmark-dot"></span>
      <span class="wordmark-name">Calmora Advisory Group</span>
    </div>
  </section>

  <section class="card card-back" aria-label="Card back">
    <div class="holder">
      <p class="holder-name">Dana Weltrup</p>
      <p class="holder-role">Managing Director</p>
      <p class="holder-role">Aerospace and Defence</p>
    </div>

    <div class="wordmark back-wordmark">
      <span class="wordmark-dot"></span>
      <span class="wordmark-name">Calmora Advisory Group</span>
    </div>

    <ul class="contacts">
      <li>
        <svg viewBox="0 0 24 24" aria-hidden="true"><path d="M6.6 10.8a15.1 15.1 0 0 0 6.6 6.6l2.2-2.2c.3-.3.7-.4 1-.2 1.1.4 2.3.6 3.6.6.6 0 1 .4 1 1V20c0 .6-.4 1-1 1A17 17 0 0 1 3 4c0-.6.4-1 1-1h3.5c.6 0 1 .4 1 1 0 1.3.2 2.5.6 3.6.1.3 0 .7-.2 1z"/></svg>
        <span>514-268-3917</span>
      </li>
      <li>
        <svg viewBox="0 0 24 24" aria-hidden="true"><path d="M3 5h18c.6 0 1 .4 1 1v12c0 .6-.4 1-1 1H3c-.6 0-1-.4-1-1V6c0-.6.4-1 1-1zm9 7.2L20 7H4z"/></svg>
        <span>dana.weltrup@calmora-example.com</span>
      </li>
      <li>
        <svg viewBox="0 0 24 24" aria-hidden="true"><path d="M12 2a10 10 0 1 0 0 20 10 10 0 0 0 0-20zm6.9 9h-3a15 15 0 0 0-1.3-5.6A8 8 0 0 1 18.9 11zM12 4.1c.9 1.2 1.8 3.4 2 6.9h-4c.2-3.5 1.1-5.7 2-6.9zM9.4 5.4A15 15 0 0 0 8.1 11h-3a8 8 0 0 1 4.3-5.6zM5.1 13h3a15 15 0 0 0 1.3 5.6A8 8 0 0 1 5.1 13zm6.9 6.9c-.9-1.2-1.8-3.4-2-6.9h4c-.2 3.5-1.1 5.7-2 6.9zm2.6-1.3a15 15 0 0 0 1.3-5.6h3a8 8 0 0 1-4.3 5.6z"/></svg>
        <span>www.calmora-example.com</span>
      </li>
    </ul>

    <div class="tagline-band">Proposals Management and Capture support for complex procurements</div>
  </section>
</body>
</html>
```